Infografik im Bereich Artikelbeschreibung für Onlineshop
Zielgruppe
Vertrieb von Saunaaustattung
Aufgabenstellung
Wird als Ergänzung für die Artikelbeschreibung im Webshop benötigt.
Ein Beispiel wo die Infografik platziert werden soll:
https://www.wolkenkessel-shop.de/Bilder/beispiel.jpg
Bildgröße ca. 1200 x 800 px
Als Hintergrund eventuell möglich teilweise oder ganz die Grafik mit den blauen Wassertropfen verwendbar?

```html
<!DOCTYPE html>
<html lang="de">
<head>
<meta charset="utf-8">
<title>Dampfgenerator – Infografik</title>
<link href="https://fonts.googleapis.com/css2?family=Roboto+Condensed:wght@500;600;700&display=swap" rel="stylesheet">
<style>
  :root{
    --brand-blue:#1c9fde;
    --brand-blue-dark:#0f7fc0;
    --ring-blue:#1b8fd6;
    --white:#ffffff;
    --bg-top:#b7d6e6;
    --bg-mid:#6fa9c8;
    --bg-bottom:#2d6e9a;
    --photo-grey:#c9cdd1;
  }
  *{box-sizing:border-box;margin:0;padding:0}
  html,body{width:1200px;height:800px;overflow:hidden}
  body{font-family:"Roboto Condensed",Arial,sans-serif;color:var(--white)}
  .canvas{position:relative;width:1200px;height:800px;overflow:hidden;
    background:linear-gradient(180deg,var(--bg-top) 0%,var(--bg-mid) 45%,var(--bg-bottom) 100%)}
  .connectors{position:absolute;inset:0}
  .hero{position:absolute;left:372px;top:172px;width:456px;height:456px;border-radius:50%;
    background:var(--white);border:16px solid var(--ring-blue);display:flex;align-items:center;justify-content:center}
  .hero-photo{width:300px;height:330px;border-radius:6px;
    background:linear-gradient(135deg,#eef0f2 0%,#bfc4c8 55%,#8c9296 100%)}
  .feature{position:absolute;height:92px;background:var(--brand-blue);display:flex;align-items:center;
    font-weight:600;font-size:21px;line-height:1.28;letter-spacing:.2px;text-transform:uppercase}
  .feature--left{left:0;width:330px;border-radius:0 46px 46px 0;padding-left:30px}
  .feature--left .icon{position:absolute;right:22px;top:50%;transform:translateY(-50%);width:58px;height:58px}
  .feature--right{left:855px;width:345px;border-radius:46px 0 0 46px;padding-left:118px}
  .feature--right .thumb{position:absolute;left:8px;top:50%;transform:translateY(-50%);width:80px;height:80px;
    border-radius:50%;background:var(--white);display:flex;align-items:center;justify-content:center}
  .thumb-photo{width:64px;height:64px;border-radius:50%;background:radial-gradient(circle,#e5e7e9,#8e9397)}
  .tab{position:absolute;width:102px;background:var(--brand-blue);display:flex;flex-direction:column;align-items:center;
    font-weight:600;font-size:10px;line-height:1.35;text-transform:uppercase;text-align:left}
  .tab--top{top:0;height:136px;border-radius:0 0 51px 51px;padding:18px 8px 0}
  .tab--bottom{top:655px;height:145px;border-radius:51px 51px 0 0;padding:18px 6px 0}
  .tab--top .label{width:100%;padding-left:4px}
  .tab--top svg{margin-top:10px}
  .tab--bottom .label{margin-top:14px;font-size:9px}
  svg{display:block}
</style>
</head>
<body>
<main class="canvas">
  <svg class="connectors" width="1200" height="800" aria-hidden="true">
    <g stroke="#fff" stroke-width="5" stroke-linecap="round">
      <line x1="330" y1="178" x2="440" y2="242"/>
      <line x1="330" y1="290" x2="392" y2="316"/>
      <line x1="330" y1="400" x2="372" y2="400"/>
      <line x1="330" y1="512" x2="394" y2="496"/>
      <line x1="330" y1="630" x2="440" y2="560"/>
      <line x1="855" y1="160" x2="760" y2="238"/>
      <line x1="855" y1="282" x2="806" y2="310"/>
      <line x1="855" y1="398" x2="828" y2="400"/>
      <line x1="855" y1="512" x2="808" y2="494"/>
      <line x1="855" y1="626" x2="760" y2="564"/>
    </g>
  </svg>

  <div class="hero"><div class="hero-photo" role="img" aria-label="Produktfoto: Dampfgenerator aus Edelstahl mit Anschlüssen"></div></div>

  <!-- Top tabs -->
  <div class="tab tab--top" style="left:330px">
    <span class="label">Thermoschutz</span>
    <svg width="44" height="50" viewBox="0 0 44 50" fill="none" stroke="#fff" stroke-width="2.5"><path d="M22 3 L40 10 V24 C40 36 31 44 22 47 C13 44 4 36 4 24 V10 Z"/><path d="M22 14 V30"/><circle cx="22" cy="33" r="4"/></svg>
  </div>
  <div class="tab tab--top" style="left:468px">
    <span class="label">Automatische Selbstreinigung</span>
    <svg width="46" height="46" viewBox="0 0 46 46" fill="#fff"><rect x="30" y="2" width="4" height="18" transform="rotate(30 32 11)"/><path d="M14 22 L30 18 L34 30 L20 42 L10 36 Z"/><circle cx="6" cy="40" r="2.5"/><circle cx="12" cy="44" r="2"/></svg>
  </div>
  <div class="tab tab--top" style="left:610px">
    <span class="label">Kompakte Größe</span>
    <svg width="50" height="44" viewBox="0 0 50 44" fill="none" stroke="#fff" stroke-width="2"><path d="M4 4 V40 H46"/><path d="M12 4 H40 V32" stroke-dasharray="3 3"/><text x="14" y="28" fill="#fff" stroke="none" font-size="12" font-family="serif">cm²</text></svg>
  </div>
  <div class="tab tab--top" style="left:757px">
    <span class="label">Gerät kocht auf ca. 100 C° hoch</span>
    <svg width="48" height="48" viewBox="0 0 48 48" fill="none" stroke="#fff" stroke-width="3"><circle cx="24" cy="24" r="20"/><circle cx="24" cy="24" r="7" stroke-width="2"/><line x1="10" y1="10" x2="38" y2="38"/></svg>
  </div>

  <!-- Left features -->
  <div class="feature feature--left" style="top:112px">Inkludierte<br>Armoaauslassdüse
    <svg class="icon" viewBox="0 0 58 58" fill="#fff"><circle cx="29" cy="28" r="14"/><circle cx="29" cy="28" r="6" fill="#1c9fde"/><path d="M12 48 L8 54 M29 48 V56 M46 48 L50 54" stroke="#fff" stroke-width="2"/></svg></div>
  <div class="feature feature--left" style="top:232px">Kurze Aufheizzeit
    <svg class="icon" viewBox="0 0 58 58" fill="none" stroke="#fff" stroke-width="2.5"><path d="M10 20 A22 22 0 1 1 8 32"/><path d="M10 12 V20 H18"/><text x="19" y="28" fill="#fff" stroke="none" font-size="11" font-family="serif">4 - 8</text><text x="21" y="40" fill="#fff" stroke="none" font-size="11" font-family="serif">min</text></svg></div>
  <div class="feature feature--left" style="top:352px">Ansteuerung von bis<br>zu zwei Duftstoffen
    <svg class="icon" viewBox="0 0 58 58" fill="#fff"><text x="0" y="40" font-size="14" font-weight="700" font-family="Arial">A</text><circle cx="22" cy="34" r="6"/><circle cx="36" cy="34" r="6"/><circle cx="29" cy="24" r="4"/><text x="46" y="40" font-size="14" font-weight="700" font-family="Arial">B</text></svg></div>
  <div class="feature feature--left" style="top:472px">Optional<br>Steuerung per App
    <svg class="icon" viewBox="0 0 58 58" fill="none" stroke="#fff" stroke-width="2.5"><rect x="14" y="4" width="24" height="42" rx="4"/><path d="M30 30 V20 a3 3 0 0 1 6 0 V32 l8 2 V50 H30 L24 40"/></svg></div>
  <div class="feature feature--left" style="top:595px">Elektronische<br>Entkalkung
    <svg class="icon" viewBox="0 0 58 58" fill="none" stroke="#fff" stroke-width="2.5"><path d="M18 22 V38 H10 L29 54 L48 38 H40 V22"/><circle cx="24" cy="14" r="3"/><circle cx="34" cy="10" r="3"/><circle cx="30" cy="30" r="3"/></svg></div>

  <!-- Right features -->
  <div class="feature feature--right" style="top:110px"><span class="thumb"><span class="thumb-photo" role="img" aria-label="Foto: Entkalkungsanschluss"></span></span>Manuelles<br>Entkalken</div>
  <div class="feature feature--right" style="top:228px;height:96px">Gehäuse<br>Edelstahl<br>S304</div>
  <div class="feature feature--right" style="top:350px"><span class="thumb"><span class="thumb-photo" role="img" aria-label="Foto: Heizstab"></span></span>Hochleistungs-<br>heizstäbe</div>
  <div class="feature feature--right" style="top:468px"><span class="thumb"><span class="thumb-photo" role="img" aria-label="Foto: Abflussventil"></span></span>Elektronisches<br>Abflussventil</div>
  <div class="feature feature--right" style="top:588px;height:100px">Steuerdisplay<br>fliesenbündig<br>einbaubar</div>

  <!-- Bottom tabs -->
  <div class="tab tab--bottom" style="left:330px">
    <svg width="40" height="52" viewBox="0 0 40 52" fill="none" stroke="#fff" stroke-width="2.5"><path d="M12 34 C4 28 4 8 20 4 C36 8 36 28 28 34 V40 H12 Z"/><path d="M13 44 H27 M15 48 H25"/></svg>
    <span class="label">Farblichtsteuerung</span>
  </div>
  <div class="tab tab--bottom" style="left:468px">
    <svg width="44" height="52" viewBox="0 0 44 52" fill="#fff"><rect x="18" y="4" width="14" height="26" rx="3" transform="rotate(25 25 17)"/><circle cx="12" cy="38" r="2"/><circle cx="18" cy="44" r="1.6"/><circle cx="8" cy="46" r="1.4"/></svg>
    <span class="label">Ansteuerung Salzsolevernebler</span>
  </div>
  <div class="tab tab--bottom" style="left:610px">
    <svg width="30" height="52" viewBox="0 0 30 52" fill="none" stroke="#fff" stroke-width="2.5"><path d="M10 32 V6 a5 5 0 0 1 10 0 V32"/><circle cx="15" cy="40" r="8"/><path d="M15 14 V36"/></svg>
    <span class="label">Verbrühschutz Abfluss</span>
  </div>
  <div class="tab tab--bottom" style="left:757px">
    <svg width="50" height="50" viewBox="0 0 50 50" fill="none" stroke="#fff" stroke-width="2.5"><circle cx="25" cy="25" r="3"/><path d="M25 22 C18 8 32 4 32 14 Z M28 27 C42 28 38 42 30 36 Z M22 27 C12 38 4 28 14 24 Z"/></svg>
    <span class="label">Integrierte Abluftsteuerung</span>
  </div>
</main>
</body>
</html>
```